a residential cleaning service needs a website

We need a website for our faith based residential cleaning service, we are called MARGOT'S CLEANING SERVICE. We want a website that is clean looking both for mobile version and desktop. We want to convey cleanliness and trust to our clients. The color scheme should go in hand with the colors of the LOGO. We would like an about page, statement of faith page, services page and also a page for a booking module that our CRM has provided for us to being able to code and dress said module is important. The website not only needs to market to new customers and convey our service but also be easy to use for existing clients to schedule cleanings and services.
Industry/Entity Type
Cleaning Service
Coding
Coded - Design and coding required
Number of Pages Required
4 page
Requirements
Must have
- About page
Statement of Faith page
services page
booking and login page

```html
<!DOCTYPE html>
<html lang="en">
<head>
<meta charset="utf-8">
<title>Margot's Cleaning Service</title>
<link rel="stylesheet" href="https://fonts.googleapis.com/css2?family=Cinzel:wght@400;500;600&family=Montserrat:wght@300;400;500;600;700&display=swap">
<style>
:root{
  --blue:#24489c;
  --blue-dark:#1c3a82;
  --ink:#1d1d1f;
  --grey:#58585a;
  --grey-text:#8a8a8a;
  --line:#d9d9d9;
  --dark:#333335;
  --white:#ffffff;
}
*{margin:0;padding:0;box-sizing:border-box}
html,body{width:1200px;height:3709px;overflow:hidden;background:var(--white)}
body{position:relative;font-family:'Montserrat',sans-serif;color:var(--ink)}
.abs{position:absolute}
.serif{font-family:'Cinzel',serif}
.btn{position:absolute;display:flex;align-items:center;justify-content:center;gap:9px;background:var(--blue);color:var(--white);font-weight:700;border-radius:40px;text-transform:uppercase;letter-spacing:.2px}
.btn .arrow{width:13px;height:13px;border-radius:50%;background:var(--white);color:var(--blue);font-size:9px;display:flex;align-items:center;justify-content:center}

/* header */
.site-header{position:absolute;left:0;top:0;width:1200px;height:90px;background:var(--white);border-top:3px solid var(--blue-dark);z-index:3}
.brand{position:absolute;left:144px;top:-10px;width:209px;height:180px;border-radius:0 0 105px 105px;background:var(--white);z-index:4;display:flex;flex-direction:column;align-items:center;justify-content:center;text-align:center}
.brand .mark{width:22px;height:22px;border-radius:50%;background:var(--blue);margin-bottom:10px}
.brand .name{font-family:'Cinzel',serif;font-weight:600;color:var(--blue);font-size:20px;line-height:1.15}
.main-nav{position:absolute;left:428px;top:36px;display:flex;gap:0;font-size:14px;font-weight:600;color:var(--ink)}
.main-nav span{margin-right:24px}
.main-nav .active{color:var(--blue)}
.login{left:949px;top:27px;width:105px;height:38px;font-size:15px}

/* hero */
.hero-photo{position:absolute;left:0;top:90px;width:1200px;height:740px;background:linear-gradient(100deg,#f2f2f2 0%,#e9ebee 40%,#d8dce2 65%,#c9ced6 100%)}
.hero-title{left:144px;top:240px;font-family:'Cinzel',serif;font-size:58px;line-height:67px;color:var(--grey);font-weight:500}
.hero-title .accent{color:var(--blue)}
.hero-call{left:144px;top:462px;display:flex;align-items:center;gap:12px;font-size:29px;font-weight:600;color:var(--ink)}
.hero-call .ring{width:54px;height:54px;border:3px solid var(--blue);border-radius:50%;display:flex;align-items:center;justify-content:center}
.hero-cta{left:144px;top:556px;width:357px;height:58px;font-size:14px}
.slider-dots{left:1119px;top:380px;display:flex;flex-direction:column;gap:13px}
.slider-dots i{width:11px;height:11px;border-radius:50%;background:#555}
.slider-dots i.on{background:var(--blue)}
.hero-curve{position:absolute;left:0;top:600px}

/* about */
.about-bg{position:absolute;left:0;top:830px;width:1200px;height:615px;background:linear-gradient(180deg,#ffffff 0%,#f5f6f7 60%,#eeeff1 100%)}
.about-photo{position:absolute;left:118px;top:943px;width:384px;height:384px;border-radius:50%;background:radial-gradient(circle at 50% 40%,#8fa37a,#5b6b4f 60%,#3f4a5a)}
.about-ring{position:absolute;left:80px;top:905px}
.section-heading{position:absolute;display:flex;align-items:center;gap:16px;font-family:'Cinzel',serif;font-weight:500;font-size:46px;color:var(--ink)}
.section-heading::before,.section-heading::after{content:"";width:84px;height:3px;background:var(--grey)}
.about-heading{left:494px;top:916px}
.about-copy{left:593px;top:1003px;width:470px;font-size:13.5px;line-height:28px;color:var(--grey-text);font-weight:400}
.about-more{left:593px;top:1292px;width:173px;height:58px;font-size:14px}

/* feature tiles */
.tile{position:absolute;top:1445px;width:400px;height:360px;display:flex;align-items:flex-end;justify-content:center;padding-bottom:58px;text-align:center;color:var(--white);font-weight:700;font-size:20px;line-height:30px}
.tile-faith{left:0;background:linear-gradient(180deg,#1e3d8f,#2f4b7a 60%,#3c5d3f)}
.tile-staff{left:400px;background:linear-gradient(180deg,#3b4046,#2a3448 55%,#1f2a44)}
.tile-value{left:800px;background:linear-gradient(160deg,#4a7de8,#2e63d8 60%,#3c5fb5)}

/* services */
.services-heading{left:342px;top:1912px}
.service-card{position:absolute;top:2027px;width:291px;height:343px;border:1px solid var(--line);border-radius:4px;background:var(--white);text-align:center;padding-top:25px}
.service-card h3{margin-top:26px;font-size:16px;font-weight:700;color:var(--ink);letter-spacing:.3px}
.service-card p{margin:18px auto 0;width:248px;font-size:12.5px;line-height:23px;color:var(--grey-text)}
.card-1{left:144px}.card-2{left:455px}.card-3{left:766px}
.card-btn{top:2348px;width:144px;height:48px;font-size:12px}

/* supply band */
.supply-grey{position:absolute;left:650px;top:2504px;width:550px;height:173px;background:var(--grey);clip-path:polygon(0 0,100% 0,100% 100%,40px 100%)}
.supply-blue{position:absolute;left:0;top:2514px;width:690px;height:154px;background:var(--blue);clip-path:polygon(0 0,651px 0,100% 100%,0 100%)}
.supply-title{left:147px;top:2565px;font-family:'Cinzel',serif;font-size:42px;font-weight:500;color:var(--white)}
.supply-note{left:696px;top:2555px;width:380px;font-size:13px;line-height:24px;color:var(--white)}

/* contact */
.contact-bg{position:absolute;left:0;top:2677px;width:1200px;height:760px;background:linear-gradient(180deg,#f1f2f3 0%,#f8f8f9 50%,#eceef0 100%)}
.contact-heading{left:315px;top:2778px}
.field{position:absolute;width:309px;height:56px;border:1px solid #cfcfcf;background:var(--white);font-size:15px;color:#777;padding:0 22px;display:flex;align-items:center}
.field.select{justify-content:space-between}
.field.select::after{content:"";border-left:5px solid transparent;border-right:5px solid transparent;border-top:6px solid #555}
.col-1{left:125px}.col-2{left:445px}.col-3{left:765px}
.row-1{top:2897px}.row-2{top:2969px}
.field.message{left:125px;top:3042px;width:950px;height:142px;align-items:flex-start;padding-top:20px}
.submit{left:481px;top:3221px;width:236px;height:65px;font-size:14px}

/* footer */
.footer-shape{position:absolute;left:0;top:3360px}
.socials{left:499px;top:3483px;display:flex;gap:5px}
.socials i{width:46px;height:46px;border-radius:50%;border:2px solid var(--white);display:flex;align-items:center;justify-content:center}
.socials i::after{content:"";width:12px;height:12px;border-radius:50%;background:var(--white)}
.footer-nav{left:0;width:1200px;top:3564px;display:flex;justify-content:center;gap:32px;color:var(--white);font-size:19px;font-weight:600}
.footer-contact{left:0;width:1200px;top:3606px;text-align:center;color:#e5e5e5;font-size:15px;display:flex;justify-content:center;align-items:center;gap:8px}
.footer-copy{left:0;width:1200px;top:3645px;text-align:center;color:#e5e5e5;font-size:15px}
</style>
</head>
<body>

<header class="site-header">
  <nav class="main-nav">
    <span class="active">HOME</span><span>ABOUT</span><span>STATEMENT OF FAITH</span><span>SERVICES</span><span>BOOKING</span>
  </nav>
  <div class="btn login">LOGIN</div>
</header>
<div class="brand"><div class="mark"></div><div class="name">MARGOT'S<br>CLEANING<br>SERVICE</div></div>

<section class="hero">
  <div class="hero-photo" role="img" aria-label="Smiling cleaner in blue apron and gloves wiping a bedside table"></div>
  <h1 class="abs hero-title">MARGOT'S<br><span class="accent">CLEANING</span><br>SERVICE</h1>
  <div class="abs hero-call">
    <span class="ring"><svg width="26" height="26" viewBox="0 0 24 24"><path d="M6.6 10.8a15 15 0 0 0 6.6 6.6l2.2-2.2c.3-.3.7-.4 1-.2 1.1.4 2.3.6 3.6.6.6 0 1 .4 1 1V20c0 .6-.4 1-1 1A17 17 0 0 1 3 4c0-.6.4-1 1-1h3.5c.6 0 1 .4 1 1 0 1.3.2 2.5.6 3.6.1.3 0 .7-.2 1z" fill="#24489c"/></svg></span>
    CALL 1 888 888 8888
  </div>
  <div class="btn hero-cta">SCHEDULE CLEANINGS AND SERVICES <span class="arrow">›</span></div>
  <div class="abs slider-dots"><i></i><i></i><i class="on"></i><i></i><i></i></div>
  <svg class="hero-curve" width="1200" height="240" viewBox="0 0 1200 240">
    <path d="M0 12 Q600 390 1200 12 V240 H0 Z" fill="#ffffff"/>
    <path d="M0 16 Q600 390 1200 16" fill="none" stroke="#58585a" stroke-width="4"/>
    <path d="M0 22 Q600 410 1200 22" fill="none" stroke="#24489c" stroke-width="7"/>
  </svg>
</section>

<section class="about">
  <div class="about-bg" role="img" aria-label="Faint background photo of a cleaner at work"></div>
  <div class="about-photo" role="img" aria-label="Worker pressure washing a garden patio"></div>
  <svg class="about-ring" width="460" height="460" viewBox="0 0 460 460">
    <path d="M12 252 A218 218 0 0 1 322 30" fill="none" stroke="#58585a" stroke-width="10"/>
    <path d="M244 26 A218 218 0 0 1 452 252" fill="none" stroke="#24489c" stroke-width="10"/>
    <path d="M50 372 A218 218 0 0 0 340 410" fill="none" stroke="#58585a" stroke-width="8"/>
    <path d="M210 402 A185 185 0 0 0 400 370" fill="none" stroke="#24489c" stroke-width="8"/>
  </svg>
  <h2 class="section-heading about-heading">ABOUT</h2>
  <p class="abs about-copy">Margot's Cleaning Service is a faith based cleaning business founded in middle Tennessee over 19 years ago. Fueled by great work and word of mouth, a part time source of income to a mother of 4 changed and grew by into a full time job. Over the years Margot's Cleaning Service has developed its cleaning process into a methodical approach where attention to detail and a continual striving for excellence presents itself in everything we do. We realize that life gets busy and sometimes cleaning is a tall hurdle to overcome, so we consider it an honor if we get to help make life a little easier.</p>
  <div class="btn about-more">READ MORE <span class="arrow">›</span></div>
</section>

<section class="features">
  <div class="tile tile-faith" role="img" aria-label="Large family house at dusk with blue overlay">STATEMENT<br>OF FAITH</div>
  <div class="tile tile-staff" role="img" aria-label="Two uniformed cleaning staff with supplies">HIGHLY TRAINED &amp; SCREENED<br>EMPLOYEES</div>
  <div class="tile tile-value" role="img" aria-label="Clean bathroom sink with blue overlay">SURPRISINGLY<br>AFFORDABLE</div>
</section>

<section class="services">
  <h2 class="section-heading services-heading">OUR SERVICES</h2>
  <article class="service-card card-1">
    <svg width="90" height="90" viewBox="0 0 90 90" fill="none" stroke="#24489c" stroke-width="3" stroke-linecap="round" stroke-linejoin="round">
      <circle cx="45" cy="45" r="42"/>
      <path d="M33 50 L45 39 L57 50 M37 47 V60 H53 V47"/>
      <path d="M45 30 V12 M40 17 L45 12 L50 17 M45 66 V78 M40 73 L45 78 L50 73 M28 45 H12 M17 40 L12 45 L17 50 M62 45 H78 M73 40 L78 45 L73 50 M33 33 L21 21 M21 28 V21 H28 M57 33 L69 21 M62 21 H69 V28"/>
    </svg>
    <h3>MOVE IN – MOVE OUT</h3>
    <p>We understand that moving is a daunting process and we are delighted to offer services if that means less stress for you. From ceiling to floor, we will take care of it!</p>
  </article>
  <article class="service-card card-2">
    <svg width="90" height="90" viewBox="0 0 90 90" fill="none" stroke="#24489c" stroke-width="3" stroke-linejoin="round">
      <path d="M22 40 H68 L64 84 H26 Z"/>
      <path d="M30 56 H60 V76 H30 Z"/>
      <path d="M48 40 V24 H58 L66 30 H56 V40"/>
      <circle cx="14" cy="20" r="4"/><circle cx="26" cy="12" r="4"/><circle cx="32" cy="26" r="5"/><circle cx="18" cy="32" r="3"/>
    </svg>
    <h3>ONE TIME CLEANING</h3>
    <p>Planning a party, hosting the in-laws, or just too busy to clean this week? We've got you covered! We offer our detailed cleaning expertise to those who aren't looking for a regular service.</p>
  </article>
  <article class="service-card card-3">
    <svg width="90" height="90" viewBox="0 0 90 90" fill="none" stroke="#24489c" stroke-width="3" stroke-linejoin="round">
      <path d="M8 60 H52 V86 H8 Z M8 72 H52"/>
      <circle cx="16" cy="80" r="3"/><circle cx="44" cy="80" r="3"/>
      <path d="M14 40 H30 V60 H14 Z M20 40 V32 H28 L32 36"/>
      <path d="M34 46 H48 V60 H34 Z"/>
      <path d="M70 4 V64 M58 64 H82 L86 86 H54 Z M62 72 V84 M70 72 V84 M78 72 V84"/>
    </svg>
    <h3>ROUTINE CLEANING SERVICE</h3>
    <p>We can design a cleaning plan for you. Once a month, bi- monthly, weekly, whatever you need we are there to help! Each cleaning service will be thorough and leave you satisfied.</p>
  </article>
  <div class="btn card-btn" style="left:217px">READ MORE <span class="arrow">›</span></div>
  <div class="btn card-btn" style="left:528px">READ MORE <span class="arrow">›</span></div>
  <div class="btn card-btn" style="left:839px">READ MORE <span class="arrow">›</span></div>
</section>

<section class="supply">
  <div class="supply-grey"></div>
  <div class="supply-blue"></div>
  <h2 class="abs supply-title">WE SUPPLY EVERYTHING</h2>
  <p class="abs supply-note">Margot's Cleaning Service provides all equipment and cleaning supplies needed to clean your home to the highest standards.</p>
</section>

<section class="contact">
  <div class="contact-bg" role="img" aria-label="Faint background photo of a cleaner wiping a surface"></div>
  <h2 class="section-heading contact-heading">CONTACT FORM</h2>
  <div class="field col-1 row-1">Enter Name</div>
  <div class="field col-2 row-1">Address</div>
  <div class="field col-3 row-1">City</div>
  <div class="field col-1 row-2">Email</div>
  <div class="field col-2 row-2">Phone Number</div>
  <div class="field select col-3 row-2">Services</div>
  <div class="field message">Message</div>
  <div class="btn submit">SUBMIT MESSAGE <span class="arrow">›</span></div>
</section>

<footer>
  <svg class="footer-shape" width="1200" height="349" viewBox="0 0 1200 349">
    <path d="M0 232 Q600 -110 1200 232 V349 H0 Z" fill="#333335"/>
    <path d="M0 226 Q600 -118 1200 226" fill="none" stroke="#24489c" stroke-width="7"/>
  </svg>
  <div class="abs socials"><i></i><i></i><i></i><i></i></div>
  <nav class="abs footer-nav"><span>HOME</span><span>ABOUT</span><span>STATEMENT OF FAITH</span><span>SERVICES</span><span>BOOKING</span></nav>
  <div class="abs footer-contact">
    <svg width="11" height="14" viewBox="0 0 12 16"><path d="M6 0a6 6 0 0 1 6 6c0 4.5-6 10-6 10S0 10.5 0 6a6 6 0 0 1 6-6zm0 3.5a2.5 2.5 0 1 0 0 5 2.5 2.5 0 0 0 0-5z" fill="#e5e5e5"/></svg>
    234,Lorem ipsum donsectetur adipiscing &nbsp;| &nbsp;
    <svg width="13" height="13" viewBox="0 0 24 24"><path d="M6.6 10.8a15 15 0 0 0 6.6 6.6l2.2-2.2c.3-.3.7-.4 1-.2 1.1.4 2.3.6 3.6.6.6 0 1 .4 1 1V20c0 .6-.4 1-1 1A17 17 0 0 1 3 4c0-.6.4-1 1-1h3.5c.6 0 1 .4 1 1 0 1.3.2 2.5.6 3.6.1.3 0 .7-.2 1z" fill="#e5e5e5"/></svg>
    Phone : 1 888 888 8888
  </div>
  <p class="abs footer-copy">© 2020 margot's cleaning service | All Rights Reserved | Privacy policy</p>
</footer>

</body>
</html>
```